Marbrook Chiropractic Center, PLLC sign

I need a design for a sign that will hang from a light post by the road and lets people know that my business is inside the big medical building nearby. I would like it to catch the eye of passing motorists. The design should fit on a sign that is 3 feet wide and 5 feet long. I am a Chiropractor and treat a wide range of patients. I would like the sign to look professional, but eyecatching.

The provided business logo is a .jpg. I can provide .eps if that would be better.
I like the colors in my Marbrook Chiropractic logo.

Marbrook Chiropractic Center, PLLC
(555) 287-4163
www.marbrookspine-example.com
If space allows, please include (listed from most important to least important to include):
• Short Term Care For Your Neck & Back Pain
• No Referral Needed
• Affordable / Insurance Accepted
• Proficient in treating Soft Tissue Problems

Industry/Entity Type

Medical

Requirements
Must have
• logos
website
phone number
Nice to have
• the bullet points
Should not have
• a spine

```html
<!DOCTYPE html>
<html lang="en">
<head>
<meta charset="utf-8">
<title>Marbrook Chiropractic – Roadside Sign</title>
<link href="https://fonts.googleapis.com/css2?family=Arimo:wght@400;700&display=swap" rel="stylesheet">
<style>
  :root {
    --brown-light: #9a4416;
    --brown-dark: #6a2608;
    --navy: #232a84;
    --white: #ffffff;
    --gold: #f2b83a;
    --cyan: #3fc3f0;
    --badge: #d9dce3;
    --photo-a: #c9b7a6;
    --photo-b: #8c8784;
  }
  * { margin: 0; padding: 0; box-sizing: border-box; }
  html, body { width: 720px; height: 1200px; overflow: hidden; background: var(--brown-dark); }
  .sign {
    position: relative;
    width: 720px;
    height: 1200px;
    overflow: hidden;
    background: radial-gradient(ellipse at 30% 55%, var(--brown-light) 0%, var(--brown-dark) 85%);
    font-family: "Arimo", Arial, sans-serif;
    color: var(--white);
  }
  .backdrop { position: absolute; inset: 0; }
  .brand-name {
    position: absolute;
    right: 20px;
    top: 124px;
    display: flex;
    align-items: center;
    gap: 10px;
    font-weight: 700;
    font-size: 32px;
    line-height: 1;
    color: var(--navy);
    white-space: nowrap;
  }
  .brand-dot {
    width: 22px; height: 22px;
    border-radius: 50%;
    background: var(--gold);
    flex: none;
  }
  .benefits {
    position: absolute;
    left: 44px;
    top: 548px;
    list-style: none;
    font-weight: 700;
    font-size: 36px;
    line-height: 39px;
  }
  .benefits li {
    position: relative;
    padding-left: 30px;
    margin-bottom: 40px;
  }
  .benefits li::before {
    content: "";
    position: absolute;
    left: 0; top: 15px;
    width: 11px; height: 11px;
    border-radius: 50%;
    background: var(--white);
  }
  .contact {
    position: absolute;
    left: 0; right: 0;
    top: 1022px;
    text-align: center;
  }
  .phone {
    display: block;
    font-weight: 700;
    font-size: 80px;
    line-height: 1;
    color: var(--gold);
  }
  .website {
    display: block;
    margin-top: 14px;
    font-weight: 400;
    font-size: 40px;
    line-height: 1;
    color: var(--cyan);
  }
</style>
</head>
<body>
<main class="sign">
  <svg class="backdrop" width="720" height="1200" viewBox="0 0 720 1200">
    <defs>
      <clipPath id="light-panel">
        <path d="M352 0 C255 90 275 235 402 315 C545 405 690 580 720 980 L720 0 Z"/>
      </clipPath>
      <linearGradient id="photo-tone" x1="0" y1="0" x2="1" y2="1">
        <stop offset="0" stop-color="var(--photo-a)"/>
        <stop offset="1" stop-color="var(--photo-b)"/>
      </linearGradient>
    </defs>
    <path class="curve-band" d="M326 0 C225 95 245 245 378 328 C515 415 668 590 720 1010 L720 0 Z" fill="var(--navy)"/>
    <path class="light-panel" d="M352 0 C255 90 275 235 402 315 C545 405 690 580 720 980 L720 0 Z" fill="var(--white)"/>
    <g clip-path="url(#light-panel)">
      <rect class="care-photo" x="430" y="200" width="290" height="450" fill="url(#photo-tone)" role="img" aria-label="Photo of a chiropractor gently adjusting a seated patient's neck"/>
    </g>
    <rect class="partner-badge" x="428" y="20" width="140" height="38" rx="19" fill="var(--badge)"/>
    <rect class="partner-badge" x="584" y="20" width="122" height="38" rx="4" fill="var(--badge)"/>
  </svg>

  <div class="brand-name">
    <span class="brand-dot"></span>
    <span>Marbrook Chiropractic</span>
  </div>

  <ul class="benefits">
    <li>Short Term Care For<br>Your Neck &amp; Back Pain</li>
    <li>No Referral Needed</li>
    <li>Affordable<br>Insurance Accepted</li>
    <li>Proficient in treating Soft<br>Tissue Problems</li>
  </ul>

  <div class="contact">
    <span class="phone">(555) 287-4163</span>
    <span class="website">www.marbrookspine-example.com</span>
  </div>
</main>
</body>
</html>
```